BRV Stationary
BRV All The Way!
Corporate
Dale Orwick
CEO
2380 Tallow St. Suite #240 San Francisco, CA 94107
dorwick@brvatw.com
brvatw.com
looking for a water mark on the business cards and stationary. Check out the brief for the logo for more ideas. http://orders.markcraftdepot.com/contests/bright-relay-ventures/readbrief

```html
<!DOCTYPE html>
<html lang="en">
<head>
<meta charset="utf-8">
<title>BRV Stationary</title>
<link href="https://fonts.googleapis.com/css2?family=Open+Sans:wght@400;600;800&display=swap" rel="stylesheet">
<style>
  :root {
    --backdrop: #5b2f1f;
    --paper: #ffffff;
    --brand-blue: #3f5ba3;
    --brand-green: #6b9d35;
    --ink: #55595f;
    --ink-soft: #8d9096;
    --night: #141414;
    --mark-faint: rgba(63, 91, 163, 0.13);
    --rule-grey: #c9ccd2;
  }
  * { margin: 0; padding: 0; box-sizing: border-box; }
  html, body { width: 1200px; height: 497px; overflow: hidden; }
  body {
    position: relative;
    background: var(--backdrop);
    font-family: "Open Sans", Arial, sans-serif;
    color: var(--ink);
  }
  .piece { position: absolute; overflow: hidden; box-shadow: 0 2px 6px rgba(0,0,0,.35); }
  .piece svg.shape { position: absolute; inset: 0; width: 100%; height: 100%; }
  .wordmark { position: absolute; font-weight: 800; letter-spacing: 1px; line-height: 1; color: var(--brand-blue); }
  .wordmark.on-colour { color: var(--paper); }
  .wordmark.faint { color: var(--mark-faint); }
  .tagline { position: absolute; font-size: 4px; letter-spacing: .6px; color: var(--ink-soft); text-transform: uppercase; }
  .small-copy { position: absolute; font-size: 4.6px; line-height: 1.45; color: var(--ink); }
  .small-copy.light { color: var(--paper); }

  /* business cards */
  .card { width: 192px; height: 108px; border-radius: 3px; }
  .card-front { left: 19px; top: 67px; background: var(--paper); }
  .card-back-dark { left: 221px; top: 67px; background: var(--brand-blue); }
  .card-blue { left: 19px; top: 192px; background: var(--brand-blue); }
  .card-green { left: 221px; top: 192px; background: var(--brand-green); }
  .card-white { left: 120px; top: 312px; background: var(--paper); }

  /* letterhead */
  .letterhead { left: 432px; top: 34px; width: 372px; height: 458px; background: var(--paper); }

  /* envelopes */
  .envelope { background: var(--paper); }
  .envelope-green { left: 739px; top: 36px; width: 449px; height: 185px; }
  .envelope-white { left: 725px; top: 163px; width: 456px; height: 197px; }
  .envelope-blue { left: 612px; top: 221px; width: 420px; height: 235px; }
</style>
</head>
<body>

<!-- card front: name side -->
<div class="piece card card-front">
  <svg class="shape" viewBox="0 0 192 108" preserveAspectRatio="none">
    <path d="M192 0 H150 C128 30 128 78 150 108 H192 Z" fill="var(--brand-blue)"/>
    <path d="M146 0 C124 30 124 78 146 108" fill="none" stroke="var(--brand-green)" stroke-width="1.5"/>
  </svg>
  <div class="small-copy" style="left:10px;top:9px;"><strong>Dale Orwick</strong><br>CEO</div>
  <div class="wordmark" style="left:72px;top:38px;font-size:24px;">BRV</div>
  <div class="tagline" style="left:66px;top:64px;">Bright Relay Ventures</div>
  <div class="small-copy" style="left:10px;top:62px;">2380 Tallow St. Suite #240<br>San Francisco, CA 94107<br>Phone: 415.555.0192<br>dorwick@brvatw.com</div>
</div>

<!-- card back: blue and dark -->
<div class="piece card card-back-dark">
  <svg class="shape" viewBox="0 0 192 108" preserveAspectRatio="none">
    <path d="M192 0 H70 C48 30 48 78 70 108 H192 Z" fill="var(--night)"/>
    <path d="M66 0 C44 30 44 78 66 108" fill="none" stroke="var(--brand-green)" stroke-width="1.5"/>
  </svg>
  <div class="wordmark on-colour" style="left:100px;top:36px;font-size:28px;">BRV</div>
  <div class="tagline" style="left:94px;top:66px;color:#c9ccd2;">Bright Relay Ventures</div>
  <div class="small-copy light" style="left:8px;top:10px;">Dale Orwick<br>CEO</div>
</div>

<!-- card back: blue -->
<div class="piece card card-blue">
  <div class="wordmark on-colour" style="left:58px;top:34px;font-size:34px;">BRV</div>
  <div class="small-copy light" style="left:78px;top:86px;">brvatw.com</div>
</div>

<!-- card back: green -->
<div class="piece card card-green">
  <div class="wordmark on-colour" style="left:58px;top:34px;font-size:34px;">BRV</div>
  <div class="small-copy light" style="left:78px;top:86px;">brvatw.com</div>
</div>

<!-- card back: white -->
<div class="piece card card-white">
  <div class="wordmark" style="left:58px;top:32px;font-size:34px;">BRV</div>
  <div class="small-copy" style="left:78px;top:86px;">brvatw.com</div>
</div>

<!-- letterhead -->
<div class="piece letterhead">
  <svg class="shape" viewBox="0 0 372 458" preserveAspectRatio="none">
    <path d="M0 62 C30 150 30 330 0 458" fill="none" stroke="var(--brand-blue)" stroke-width="3"/>
    <path d="M0 58 C38 150 38 330 6 458" fill="none" stroke="var(--brand-green)" stroke-width="1.5"/>
  </svg>
  <div class="wordmark" style="left:18px;top:18px;font-size:34px;">BRV</div>
  <div class="tagline" style="left:20px;top:52px;">Bright Relay Ventures</div>
  <div class="small-copy" style="left:262px;top:20px;">2380 Tallow St.<br>Suite #240<br>San Francisco, CA 94107<br>Phone: 415.555.0192<br>brvatw.com</div>
  <div class="wordmark faint" style="left:112px;top:196px;font-size:62px;">BRV</div>
</div>

<!-- green envelope -->
<div class="piece envelope envelope-green">
  <svg class="shape" viewBox="0 0 449 185" preserveAspectRatio="none">
    <path d="M0 0 H449 V32 C320 50 130 50 0 32 Z" fill="var(--brand-green)"/>
  </svg>
  <div class="wordmark on-colour" style="left:200px;top:4px;font-size:22px;">BRV</div>
</div>

<!-- white envelope -->
<div class="piece envelope envelope-white">
  <svg class="shape" viewBox="0 0 456 197" preserveAspectRatio="none">
    <path d="M0 0 L228 70 L456 0" fill="none" stroke="var(--rule-grey)" stroke-width="1.2"/>
  </svg>
  <div class="wordmark" style="left:160px;top:20px;font-size:24px;">BRV</div>
  <div class="wordmark faint" style="left:350px;top:140px;font-size:34px;">BRV</div>
</div>

<!-- blue envelope -->
<div class="piece envelope envelope-blue">
  <svg class="shape" viewBox="0 0 420 235" preserveAspectRatio="none">
    <path d="M0 0 H420 V40 C300 100 120 100 0 40 Z" fill="var(--brand-blue)"/>
    <path d="M0 44 C120 104 300 104 420 44" fill="none" stroke="var(--brand-green)" stroke-width="1.2"/>
  </svg>
  <div class="wordmark" style="left:20px;top:102px;font-size:28px;">BRV</div>
  <div class="tagline" style="left:22px;top:132px;">Bright Relay Ventures</div>
  <div class="small-copy" style="left:22px;top:172px;">2380 Tallow St.<br>Suite #240<br>San Francisco, CA 94107<br>brvatw.com</div>
  <div class="wordmark faint" style="left:300px;top:176px;font-size:38px;">BRV</div>
</div>

</body>
</html>
```